Gourmet Tea Shop needs new website

I need a new professional looking web design for my retail tea store. I would like all the big commerce functionalities set up eg shipping, payment gateway etc. The current website is www.hollowbrookparlour.com and I would like the existing materials uploaded into the new website

Target Market(s)

tea lovers

Industry/Entity Type

Shipping

Number of Pages Required

5+ page

Requirements
Must have
• I leave this to the web designer's discretion
Nice to have
Should not have

```html
<!DOCTYPE html>
<html lang="en">
<head>
<meta charset="utf-8">
<title>Hollowbrook Parlour – Tea Shop</title>
<link rel="stylesheet" href="https://fonts.googleapis.com/css2?family=Questrial&family=Mulish:wght@400;700;800&display=swap">
<style>
:root{
  --topbar:#ececec;
  --upper:#e2e5dd;
  --page:#e4e7df;
  --page-light:#eaece6;
  --green:#9cbd67;
  --green-dark:#6f9a3d;
  --green-pale:#d7e2c4;
  --footer:#cbdbb3;
  --footer-light:#d3e1bd;
  --text:#555a50;
  --muted:#8a8f85;
  --card-border:#d6d9d2;
}
*{box-sizing:border-box;margin:0;padding:0}
html,body{width:959px;height:1200px;overflow:hidden}
body{
  position:relative;font-family:"Questrial",sans-serif;color:var(--text);
  background:linear-gradient(var(--page-light),var(--page));
}
.abs{position:absolute}
.topbar{left:0;top:0;width:959px;height:43px;background:var(--topbar);border-bottom:2px solid #fff;box-shadow:0 1px 2px rgba(0,0,0,.08)}
.social{top:12px;display:flex;gap:8px;left:173px}
.social span{width:21px;height:21px;border-radius:50%;background:#f6f6f6;border:1px solid #c9c9c9}
.account{top:19px;right:173px;display:flex;gap:18px;font-size:8px;color:#8b8b8b;text-transform:uppercase}
.account span::before{content:"";display:inline-block;width:8px;height:8px;background:#a5a5a5;border-radius:2px;margin-right:4px;vertical-align:-1px}
.upper-svg{left:0;top:45px}
.brand{left:170px;top:82px;width:150px;display:flex;align-items:center;gap:6px}
.brand .mark{width:10px;height:10px;border-radius:50%;background:var(--green-dark);flex:none}
.brand .name{font-size:15px;color:#5f6158;white-space:nowrap}
.nav{top:62px;left:336px;display:flex;align-items:center;font-size:11.5px;color:#4c4e48;text-transform:uppercase}
.nav a{color:inherit;text-decoration:none;padding:7px 14px}
.nav a.active{background:linear-gradient(#fff,#e6e6e6);border-radius:14px;box-shadow:0 2px 3px rgba(0,0,0,.18);padding:7px 17px}
.hero{left:169px;top:94px}
.dots{top:364px;left:442px;display:flex;gap:6px}
.dots span{width:15px;height:15px;border-radius:50%;border:2px solid #fff;background:#d0d5c9;box-shadow:0 0 2px rgba(0,0,0,.2)}
.searchbar{left:171px;top:387px;width:616px;height:31px;background:#d9dfcf}
.search-tag{left:0;top:0;height:31px;width:75px;background:var(--green);color:#fff;font-size:10px;line-height:31px;padding-left:15px;clip-path:polygon(0 0,100% 0,88% 50%,100% 100%,0 100%)}
.field{top:8px;height:17px;border:1px solid #b9bcb4;background:#f3f3f0;font-size:7.5px;color:#9a9d95;line-height:15px;padding-left:6px;border-radius:2px}
.pill{top:8px;height:16px;width:52px;border-radius:50%;background:linear-gradient(#fff,#e4e4e4);box-shadow:0 1px 2px rgba(0,0,0,.3);font-size:7px;text-align:center;line-height:16px;color:#555}
.found{left:173px;top:429px;width:613px;height:24px;background:#e3e8dc;font-size:9px;color:var(--green-dark);line-height:24px;padding-left:29px}
.found::before{content:"";position:absolute;left:9px;top:8px;width:7px;height:7px;border-right:2px solid var(--green);border-top:2px solid var(--green);transform:rotate(45deg)}
.card{width:142px;height:173px;background:#f2f2f0;border:1px solid var(--card-border);border-radius:3px;box-shadow:0 0 3px rgba(0,0,0,.08)}
.card .photo{position:absolute;left:8px;top:10px;width:125px;height:87px;background:var(--green)}
.card .price{position:absolute;left:8px;top:97px;width:125px;height:22px;background:var(--green-pale);font-size:15px;color:#333;text-align:right;padding-right:6px;line-height:22px}
.card .price i{position:absolute;left:5px;top:5px;width:14px;height:12px;border:2px solid #444;border-top-width:4px;border-radius:2px}
.card h3{position:absolute;top:136px;width:100%;text-align:center;font-size:10.5px;color:#7d8078;font-family:"Mulish",sans-serif;font-weight:700}
.card p{position:absolute;top:151px;width:100%;text-align:center;font-size:7.5px;color:#a2a59d}
.pager{top:853px;left:368px;display:flex;align-items:center;gap:7px;font-size:8px}
.pager b{width:19px;height:18px;border-radius:2px;background:linear-gradient(#fafafa,#d8d8d8);box-shadow:0 1px 2px rgba(0,0,0,.3);text-align:center;line-height:18px;font-weight:400;color:#444}
.pager b.on{background:linear-gradient(#cfe3a8,#9cbd67)}
.pager .gap{width:18px}
.pager .arrow{width:10px;height:10px;border-left:3px solid #bcd39a;border-bottom:3px solid #bcd39a;transform:rotate(45deg)}
.pager .arrow.next{transform:rotate(-135deg)}
.footer{left:0;top:919px;width:959px;height:281px;background:linear-gradient(var(--footer-light),var(--footer));border-top:3px solid #d8e4c6}
.col{top:28px;width:145px;font-size:7.5px;line-height:12px;color:#3f4238}
.col h4{font-family:"Mulish",sans-serif;font-weight:800;font-size:10px;color:#f7f9f2;text-shadow:0 1px 1px rgba(0,0,0,.35);margin-bottom:12px;text-transform:uppercase}
.col h4.dark{color:#2f312c;text-shadow:none}
.col p{margin-bottom:8px}
.pay{left:272px;top:150px}
.footnav{top:212px;width:959px;text-align:center;font-size:7.5px;color:#3f4238}
</style>
</head>
<body>
<svg class="abs upper-svg" width="959" height="200" aria-hidden="true">
  <path d="M0 0H959V135Q480 240 0 135Z" fill="var(--upper)"/>
  <path d="M0 135Q480 240 959 135" fill="none" stroke="#fff" stroke-width="3"/>
</svg>

<header>
  <div class="abs topbar"></div>
  <div class="abs social"><span></span><span></span><span></span></div>
  <div class="abs account"><span>Register</span><span>Signin</span><span>Whishlist</span><span>Cart</span></div>
  <div class="abs brand"><div class="mark"></div><div class="name">Hollowbrook Parlour</div></div>
  <nav class="abs nav"><a class="active">Home</a><a>Products</a><a>Buy</a><a>Blog</a><a>Shipping &amp; Returns</a><a>Contact</a></nav>
</header>

<svg class="abs hero" width="622" height="262">
  <ellipse cx="311" cy="131" rx="310" ry="130" fill="#f4f5f1" stroke="#d6d9d1"/>
  <ellipse cx="311" cy="131" rx="304" ry="124" fill="var(--green)" role="img" aria-label="Featured tea slideshow image"/>
</svg>
<div class="abs dots"><span></span><span></span><span></span><span></span></div>

<div class="abs searchbar">
  <div class="abs search-tag">SEARCH</div>
  <div class="abs field" style="left:130px;width:130px">ENTER KEYWORD</div>
  <div class="abs field" style="left:276px;width:130px">BY CATEGORY</div>
  <div class="abs pill" style="left:421px">NEW</div>
  <div class="abs pill" style="left:488px">POPULAR</div>
  <div class="abs pill" style="left:556px">PRICE</div>
</div>
<div class="abs found">We found 12 items!</div>

<main>
  <div class="abs card" style="left:173px;top:464px"><div class="photo" role="img" aria-label="Tea product photo"></div><div class="price"><i></i>$ 23.00</div><h3>Lorem ipsum dolor</h3><p>Suspendisse a pellentesque dui</p></div>
  <div class="abs card" style="left:330px;top:464px"><div class="photo" role="img" aria-label="Tea product photo"></div><div class="price"><i></i>$ 80.00</div><h3>Lorem ipsum dolor</h3><p>Suspendisse a pellentesque dui</p></div>
  <div class="abs card" style="left:487px;top:464px"><div class="photo" role="img" aria-label="Tea product photo"></div><div class="price"><i></i>$ 20.00</div><h3>Lorem ipsum dolor</h3><p>Suspendisse a pellentesque dui</p></div>
  <div class="abs card" style="left:644px;top:464px"><div class="photo" role="img" aria-label="Tea product photo"></div><div class="price"><i></i>$ 12.00</div><h3>Lorem ipsum dolor</h3><p>Suspendisse a pellentesque dui</p></div>
  <div class="abs card" style="left:173px;top:654px"><div class="photo" role="img" aria-label="Tea product photo"></div><div class="price"><i></i>$ 55.00</div><h3>Lorem ipsum dolor</h3><p>Suspendisse a pellentesque dui</p></div>
  <div class="abs card" style="left:330px;top:654px"><div class="photo" role="img" aria-label="Tea product photo"></div><div class="price"><i></i>$ 10.00</div><h3>Lorem ipsum dolor</h3><p>Suspendisse a pellentesque dui</p></div>
  <div class="abs card" style="left:487px;top:654px"><div class="photo" role="img" aria-label="Tea product photo"></div><div class="price"><i></i>$ 45.00</div><h3>Lorem ipsum dolor</h3><p>Suspendisse a pellentesque dui</p></div>
  <div class="abs card" style="left:644px;top:654px"><div class="photo" role="img" aria-label="Tea product photo"></div><div class="price"><i></i>$ 16.00</div><h3>Lorem ipsum dolor</h3><p>Suspendisse a pellentesque dui</p></div>

  <div class="abs pager"><span class="arrow"></span><b>1</b><b>2</b><b class="on">3</b><span class="gap"></span><b>4</b><b>5</b><b>6</b><span class="arrow next"></span></div>
</main>

<footer class="abs footer">
  <div class="abs col" style="left:173px"><h4>Lorem ipsum</h4><p>Vestibulum commodo volutpat a, convallis ac, laoreet enim.</p><p>Phasellus fermentum in, dolor. Pellentesque facilisis. Nulla imperdiet sit amet magna.</p></div>
  <div class="abs col" style="left:330px"><h4>Suspendisse</h4><p>- Pellentesque facilisis. Nulla imperdiet sit amet magna.<br>- Vestibulum dapibus, mauris nec malesuada fames ac turpis velit, rhoncus eu.<br>- Luctus et interdum</p></div>
  <div class="abs col" style="left:487px"><h4>Nulla imperdie</h4><p>Aliquam erat ac ipsum. Integer aliquam purus. Quisque lorem tortor fringilla sed, vestibulum id, eleifend justo vel bibendum sapien massa ac turpis. Maecenas malesuada elit lectus felis, malesuada ultricies.</p></div>
  <div class="abs col" style="left:644px;width:170px"><h4 class="dark">Contact</h4><p>Tel: 5550148273<br>Fax: 5550148273</p><p>Address:<br>E-mail: www.hollowbrookparlour.com/</p></div>
  <svg class="abs pay" width="415" height="40" aria-hidden="true">
    <ellipse cx="200" cy="22" rx="200" ry="16" fill="#d8e3c8"/>
    <ellipse cx="200" cy="24" rx="80" ry="5" fill="#9aa88a" opacity=".4"/>
    <rect x="145" y="4" width="30" height="19" rx="2" fill="#f7f4ea" stroke="#c8c3b3"/>
    <rect x="187" y="4" width="30" height="19" rx="2" fill="#f7f4ea" stroke="#c8c3b3"/>
    <rect x="230" y="4" width="30" height="19" rx="2" fill="#f7f4ea" stroke="#c8c3b3"/>
  </svg>
  <div class="abs footnav">HOME &nbsp;|&nbsp; PRODUCTS &nbsp;|&nbsp; BUY &nbsp;|&nbsp; BLOG &nbsp;|&nbsp; SHIPPING &amp; RETURN &nbsp;|&nbsp; CONTACT</div>
</footer>
</body>
</html>
```